Business Card Design Project

Looking to update our business cards. We have a logo with our slogan. We are an IT firm so we wouldlike a modern look.

Industry/Entity Type

Business

```html
<!DOCTYPE html>
<html lang="en">
<head>
<meta charset="utf-8">
<title>Norvik Inc — Business Cards</title>
<link rel="stylesheet" href="https://fonts.googleapis.com/css2?family=Jost:wght@500&family=Tinos&display=swap">
<style>
  :root {
    --backdrop: #3a2a22;
    --green-light: #9dbd41;
    --green-mid: #85a73c;
    --green-edge: #6a8b35;
    --green-ink: #52702b;
    --band-top: #ececec;
    --band-bottom: #d6d6d6;
    --ink: #222222;
  }
  * { margin: 0; padding: 0; box-sizing: border-box; }
  html, body { width: 1200px; height: 1181px; overflow: hidden; }
  body { background: var(--backdrop); position: relative; }

  .card {
    position: absolute;
    left: 200px;
    background: radial-gradient(ellipse 55% 70% at 50% 42%, var(--green-light) 0%, var(--green-mid) 45%, var(--green-edge) 100%);
    box-shadow: 0 6px 14px rgba(0,0,0,0.45);
    overflow: hidden;
  }
  .card--front { top: 97px; width: 800px; height: 460px; }
  .card--back  { top: 621px; width: 795px; height: 457px; }

  .band {
    position: absolute;
    left: 0; right: 0;
    background: linear-gradient(to bottom, var(--band-top), var(--band-bottom));
    box-shadow: 0 2px 4px rgba(0,0,0,0.3);
  }
  .card--front .band { top: 173px; height: 115px; }
  .card--back .band  { top: 172px; height: 114px; }

  .brand {
    position: absolute;
    left: 0; right: 0; top: 20px;
    text-align: center;
    font-family: "Jost", sans-serif;
    font-weight: 500;
    color: var(--green-ink);
  }
  .brand__name {
    display: inline-flex;
    align-items: center;
    gap: 12px;
    font-size: 48px;
    letter-spacing: 9px;
    line-height: 1;
  }
  .brand__dot {
    width: 16px; height: 16px;
    border-radius: 50%;
    background: var(--green-light);
  }
  .brand__tagline {
    margin-top: 13px;
    font-size: 16px;
    letter-spacing: 6px;
    color: var(--ink);
  }

  .contacts {
    position: absolute;
    top: 50px;
    left: 63px; right: 50px;
    display: flex;
    justify-content: space-between;
    font-family: "Tinos", serif;
    font-size: 17px;
    color: var(--ink);
  }
  .contact { display: flex; align-items: center; gap: 9px; }
  .contact__mark { width: 9px; height: 9px; background: var(--ink); }
</style>
</head>
<body>
  <section class="card card--front">
    <div class="band">
      <div class="brand">
        <div class="brand__name"><span>NORVIK INC</span><span class="brand__dot"></span></div>
        <div class="brand__tagline">MAKING IT SUPPORT SIMPLE</div>
      </div>
    </div>
  </section>

  <section class="card card--back">
    <div class="band">
      <div class="contacts">
        <div class="contact"><span>Phone</span><span class="contact__mark"></span><span>0123456789</span></div>
        <div class="contact"><span>Web</span><span class="contact__mark"></span><span>www.website.com</span></div>
        <div class="contact"><span>Email</span><span class="contact__mark"></span><span>name@email.com</span></div>
      </div>
    </div>
  </section>
</body>
</html>
```